Manufacturers Catalog Cover Page

We are looking to have a cover to our catalog page designed. I currently have begun work for the remained of the catalog in InDesign and want the cover created in InDesign. I will provide photos.

Looking to beable to add the cover to our existing attached catalog.

Industry/Entity Type

Manufacturing

Requirements
Must have
• Colors match what we are currently using. The Dark grey and gold
Nice to have
• modern, clean

```html
<!DOCTYPE html>
<html lang="en">
<head>
<meta charset="utf-8">
<title>Rubber &amp; Plastic Extrusion – Catalog Cover</title>
<link rel="stylesheet" href="https://fonts.googleapis.com/css2?family=Bebas+Neue&family=Open+Sans:wght@300;400;700&display=swap">
<style>
  :root {
    --charcoal: #333333;
    --gold: #dfbe78;
    --paper: #ffffff;
    --backdrop: #d9d9d9;
    --ink: #444444;
    --muted: #9a9a9a;
    --fine: #8a8a8a;
  }
  html, body {
    margin: 0;
    width: 1200px;
    height: 1200px;
    overflow: hidden;
    background: var(--backdrop);
  }
  .cover {
    position: absolute;
    left: 178px;
    top: 30px;
    width: 1075px;
    height: 1411px;
    background: var(--paper);
    transform: scale(0.8);
    transform-origin: 0 0;
    overflow: hidden;
    font-family: "Open Sans", sans-serif;
  }
  .cover-shapes {
    position: absolute;
    inset: 0;
  }
  .series-label {
    position: absolute;
    left: 127px;
    top: 28px;
    margin: 0;
    font-family: "Bebas Neue", sans-serif;
    font-weight: 400;
    font-size: 47px;
    line-height: 1;
    color: var(--paper);
  }
  .title-block {
    position: absolute;
    top: 356px;
    left: 529px;
    margin: 0;
    font-family: "Bebas Neue", sans-serif;
    font-weight: 400;
    line-height: 0.82;
  }
  .title-main {
    display: block;
    font-size: 76px;
    color: #000;
  }
  .title-sub {
    display: block;
    margin-left: 96px;
    font-size: 76px;
    color: var(--gold);
  }
  .tagline {
    position: absolute;
    left: 87px;
    top: 755px;
    margin: 0;
    font-weight: 400;
    font-size: 35px;
    line-height: 48px;
    letter-spacing: -0.5px;
    color: var(--ink);
  }
  .intro {
    position: absolute;
    left: 89px;
    top: 977px;
    width: 620px;
  }
  .intro-heading {
    margin: 0;
    font-weight: 700;
    font-size: 25px;
    line-height: 1.2;
    letter-spacing: -0.3px;
    color: var(--ink);
  }
  .intro-text {
    margin: 4px 0 0;
    font-weight: 400;
    font-size: 25px;
    line-height: 34px;
    color: var(--muted);
  }
  .feature-note {
    position: absolute;
    top: 1181px;
    margin: 0;
    font-size: 7.5px;
    line-height: 9.5px;
    color: var(--fine);
  }
  .note-1 { left: 103px; }
  .note-2 { left: 252px; }
  .note-3 { left: 401px; }
</style>
</head>
<body>
<main class="cover">
  <svg class="cover-shapes" width="1075" height="1411" viewBox="223 37 1075 1411" aria-hidden="false">
    <!-- header band -->
    <rect x="223" y="37" width="1075" height="94" fill="var(--charcoal)"/>
    <polygon points="282,58 330,85 282,112" fill="var(--gold)"/>
    <!-- corner wedges -->
    <polygon points="1072,131 1298,131 1298,357" fill="var(--charcoal)"/>
    <polygon points="304,332 579,332 579,607" fill="var(--gold)"/>
    <polygon points="1013,971 1222,971 1222,1180" fill="var(--gold)"/>
    <polygon points="887,593 1222,593 1222,928" fill="var(--charcoal)"/>
    <!-- photo area -->
    <defs>
      <linearGradient id="photoTone" x1="0" y1="0" x2="1" y2="1">
        <stop offset="0" stop-color="#6b5a40"/>
        <stop offset="0.35" stop-color="#b7a9b8"/>
        <stop offset="0.6" stop-color="#7d6a4a"/>
        <stop offset="1" stop-color="#4a4236"/>
      </linearGradient>
    </defs>
    <polygon points="596,328 1222,954 596,954" fill="url(#photoTone)" role="img" aria-label="Photo of a spool of extruded rubber strip mounted on a production machine"/>
    <!-- footer band -->
    <polygon points="223,1230 397,1401 1298,1401 1298,1448 223,1448" fill="var(--gold)"/>
    <!-- feature icons -->
    <g class="feature-icons">
      <circle cx="379" cy="1176" r="31" fill="var(--gold)"/>
      <circle cx="379" cy="1169" r="5" fill="#fff"/>
      <path d="M370,1182 q0,-8 9,-8 q9,0 9,8 z" fill="#fff"/>
      <circle cx="525" cy="1176" r="31" fill="var(--gold)"/>
      <circle cx="527" cy="1173" r="5.5" fill="none" stroke="#fff" stroke-width="2.2"/>
      <line x1="523" y1="1177" x2="518" y2="1182" stroke="#fff" stroke-width="2.6" stroke-linecap="round"/>
      <circle cx="676" cy="1176" r="31" fill="var(--gold)"/>
      <path d="M666,1177 l10,-9 l10,9 h-3 v7 h-4 v-5 h-6 v5 h-4 v-7 z" fill="#fff"/>
    </g>
  </svg>

  <h2 class="series-label">Rubber &amp; Plastic Extursion</h2>

  <h1 class="title-block">
    <span class="title-main">Main Title Here</span>
    <span class="title-sub">Cover Design</span>
  </h1>

  <p class="tagline">LOREM IPSUM<br>CONSECTETUER<br>DOLOR SIT AMET</p>

  <section class="intro">
    <h3 class="intro-heading">LOREM IPSUM DOLOR SIT AMET</h3>
    <p class="intro-text">Lorem ipsum dolor sit amet, consectetur adipis<br>or incididunt ut labore et dolore magna aliq</p>
  </section>

  <p class="feature-note note-1">Lorem ipsum dolor sit amet, qu<br>ix ei idque intellegat referren</p>
  <p class="feature-note note-2">Lorem ipsum dolor sit amet, qu<br>ix ei idque intellegat referren</p>
  <p class="feature-note note-3">Lorem ipsum dolor sit amet, qu<br>ix ei idque intellegat referren</p>
</main>
</body>
</html>
```